Young, dynamic furniture company requires leaflet design

We require a new leaflet for our modern furniture company which supplies furniture and appliances to the property and development market.
Bramwell Furniture has become one of the leading furniture & appliance suppliers to the property market withing London. With over 10 years experience, we have increased our business to supply not only Private Landlords and Managing Agents, but also Property Developers, Housing Associations and Local Councils.
We offer not only a complete range of furniture which includes beds, wardrobes, dining sets and sofas, but also a high quality, full delivery and assembly service to help you with all our furnishing needs.

Target Market(s)

Private Landlords, Developers, Letting & Managing Agents

Industry/Entity Type

Furniture Store

Font styles to use
Sans Serif

Colors
0255a3
3176b5
85abd2
cfdeed
eaf1f7

Requirements
Must have
• Contact details,
• Our services:
• FREE next day delivery within the M25
• Free furniture assembly
• Free key pick up & drop off
• Free furniture removal (on a like-for-like basis)
• All types of furniture supplied - from basic to luxury

```html
<!DOCTYPE html>
<html lang="en">
<head>
<meta charset="utf-8">
<title>Bramwell Furniture – Leaflet</title>
<link href="https://fonts.googleapis.com/css2?family=Roboto+Condensed:wght@300;400;700&display=swap" rel="stylesheet">
<style>
  :root {
    --brand-blue: #0255a3;
    --mid-blue: #3176b5;
    --soft-blue: #85abd2;
    --pale-blue: #cfdeed;
    --mist: #eaf1f7;
    --navy: #1c3a6e;
    --deep-navy: #1b2452;
    --lavender: #6f7fc0;
    --plum: #4b1b4e;
    --slate: #8a9aae;
    --paper: #f4f5f7;
    --ink: #3c3f4a;
    --backdrop: #d9dbde;
  }
  * { box-sizing: border-box; margin: 0; padding: 0; }
  html, body { width: 1200px; height: 800px; overflow: hidden; }
  body {
    background: var(--backdrop);
    font-family: "Roboto Condensed", "Arial Narrow", sans-serif;
    position: relative;
  }
  .leaflet {
    position: absolute; left: 340px; top: 32px;
    width: 520px; height: 736px;
    background: var(--paper);
    overflow: hidden;
    box-shadow: 0 6px 18px rgba(0,0,0,.18);
  }
  .hero-photo {
    position: absolute; left: 0; top: 0; width: 520px; height: 428px;
    background: linear-gradient(160deg, #b9c3d3 0%, #8f9db6 35%, #d9dcdf 60%, #9a8f86 80%, #e4e4e2 100%);
  }
  .hero-panel { position: absolute; left: 0; top: 0; }
  .brand {
    position: absolute; left: 26px; top: 26px; color: #fff;
    display: flex; align-items: center; gap: 10px;
  }
  .brand-mark { width: 18px; height: 18px; background: var(--soft-blue); }
  .brand-name { font-size: 19px; font-weight: 400; letter-spacing: .5px; }
  .brand-tagline {
    position: absolute; left: 54px; top: 52px; color: var(--pale-blue);
    font-size: 9px; letter-spacing: 1px;
  }
  .ranges { position: absolute; left: 26px; top: 84px; list-style: none; }
  .ranges li {
    height: 27px; margin-bottom: 6px; color: #fff;
    font-size: 14px; letter-spacing: .5px; line-height: 27px; padding-left: 10px;
  }
  .r-sofas { background: var(--brand-blue); width: 120px; }
  .r-beds { background: var(--deep-navy); width: 112px; }
  .r-bedroom { background: var(--lavender); width: 150px; }
  .r-dining { background: var(--mid-blue); width: 126px; }
  .r-appliances { background: var(--slate); width: 146px; }
  .r-packages { background: var(--plum); width: 160px; }

  .promise {
    position: absolute; left: 0; top: 448px; width: 520px;
    text-align: center; color: var(--navy);
    font-weight: 300; font-size: 46px; letter-spacing: 1px;
  }
  .services {
    position: absolute; left: 0; top: 516px; width: 520px;
    display: flex; justify-content: center; gap: 22px; list-style: none;
  }
  .service {
    width: 92px; height: 92px; border-radius: 50%; color: #fff;
    display: flex; flex-direction: column; align-items: center; justify-content: center;
    text-align: center; font-size: 10px; line-height: 1.15; letter-spacing: .4px;
  }
  .service strong { font-size: 17px; font-weight: 400; margin-bottom: 2px; }
  .s-delivery { background: var(--brand-blue); }
  .s-assembly { background: var(--lavender); }
  .s-removal { background: var(--plum); }
  .s-keys { background: var(--mid-blue); }

  .rule {
    position: absolute; left: 30px; top: 628px; width: 460px; height: 3px;
    background: var(--brand-blue);
  }
  .range-line {
    position: absolute; left: 0; top: 637px; width: 520px; text-align: center;
    color: var(--ink); font-size: 14px; letter-spacing: .3px;
  }
  .contact {
    position: absolute; left: 30px; top: 666px; width: 460px;
    display: flex; justify-content: space-between; font-size: 10.5px;
    color: var(--ink); line-height: 1.35;
  }
  .label { color: var(--brand-blue); font-weight: 700; }
  .web { color: var(--brand-blue); letter-spacing: 2px; }
  .hours { text-align: right; }
  .footer-band {
    position: absolute; left: 0; bottom: 0; width: 520px; height: 12px;
    background: var(--mid-blue);
  }
</style>
</head>
<body>
  <article class="leaflet">
    <div class="hero-photo" role="img" aria-label="Photograph of a bright bedroom with a white wooden bed, folded throw, bedside lamp and framed prints"></div>

    <svg class="hero-panel" width="520" height="428" viewBox="0 0 520 428" aria-hidden="true">
      <polygon points="0,0 200,0 200,290 0,368" fill="var(--navy)"/>
    </svg>

    <div class="brand">
      <span class="brand-mark"></span>
      <span class="brand-name">BRAMWELL FURNITURE</span>
    </div>
    <div class="brand-tagline">TRADE FURNITURE SOLUTIONS</div>

    <ul class="ranges">
      <li class="r-sofas">SOFAS</li>
      <li class="r-beds">BEDS</li>
      <li class="r-bedroom">BEDROOM FURNITURE</li>
      <li class="r-dining">DINING</li>
      <li class="r-appliances">APPLIANCES</li>
      <li class="r-packages">FURNITURE PACKAGES</li>
    </ul>

    <h1 class="promise">THE BF PROMISE</h1>

    <ul class="services">
      <li class="service s-delivery"><strong>FREE</strong>NEXT DAY<br>DELIVERY</li>
      <li class="service s-assembly"><strong>FREE</strong>FURNITURE<br>ASSEMBLY</li>
      <li class="service s-removal"><strong>FREE</strong>FURNITURE<br>REMOVAL</li>
      <li class="service s-keys"><strong>FREE</strong>KEY PICK UP &amp;<br>DROP OFF</li>
    </ul>

    <div class="rule"></div>
    <p class="range-line">ALL TYPES OF FURNITURE SUPPLIED - FROM BASIC TO LUXURY</p>

    <footer class="contact">
      <div class="showroom">
        <div class="label">Showroom:</div>
        <div>Unit 4 Larchmere Trade Park,</div>
        <div>Holloway Lane, London N9 0ZZ</div>
      </div>
      <div class="lines">
        <div>T: 020 7946 0321</div>
        <div>F: 020 7946 0322</div>
        <div class="web">www.bramwellfurniture.co.uk</div>
      </div>
      <div class="hours">
        <div class="label">Opening Times:</div>
        <div>Mon - Fri: 9am - 6pm</div>
        <div>Sat: 10am - 5pm</div>
        <div>Sun: 11am - 5pm</div>
      </div>
    </footer>

    <div class="footer-band"></div>
  </article>
</body>
</html>
```